Harbourline Strategy Group firm

I need a business card that is succint for a Brisbane based business called Harbourline Strategy Group Pty Ltd.
We bridge the gaps between People, Process and Technology.

We are a specialist operational excellence firm, delivering strategic consulting and business advisory services in six core capabilities, across all industries and all business lines to improve performance, efficiency, profitability, automation and scalability, for clients across Australia &New Zealand.
Updates

Hi Designers, I have uploaded the logo in 3D .png format, to assist in card design.

Target Market(s)

Project Management professionals, IT professionals, corporate and government clients managing transitioning or transformation projects.

Contact Information for Business Card

Harbourline Strategy Group Pty Ltd

Daniel Ferreira
Principal Consultant

mobile: +61 417 260 315
email: daniel@harbourlinestrategygroup.com.au
webpage: www.harbourlinestrategygroup.com

professional services: strategic advisors,

Font styles to use
Sans Serif

Requirements
Must have
• Business name: Harbourline Strategy Group
logo: attached
Contact person: Daniel Ferreira
Title: Principal Consultant
contact details:
mobile +61 417 260
email: daniel@HarbourlineStrategyGroup.com.au
website: HarbourlineStrategyGroup.com

on back side with logo include: A.B.N. 58210947362

professional services offered: Business Analysis, Strategic Advisory
Nice to have
• QR code
Should not have
• contacts picture

```html
<!DOCTYPE html>
<html lang="en">
<head>
<meta charset="utf-8">
<title>Harbourline Strategy Group – Business Card</title>
<link rel="stylesheet" href="https://fonts.googleapis.com/css2?family=Barlow+Condensed:wght@500&display=swap">
<style>
  :root {
    --navy: #222c48;
    --red: #e4282c;
    --card: #f1f1f3;
    --page: #ffffff;
    --shadow: rgba(0, 0, 0, 0.55);
  }
  * { margin: 0; padding: 0; box-sizing: border-box; }
  html, body {
    width: 1200px;
    height: 1100px;
    overflow: hidden;
    background: var(--page);
  }
  body {
    position: relative;
    font-family: "Barlow Condensed", "Arial Narrow", sans-serif;
    font-weight: 500;
    color: var(--navy);
  }
  .swatch {
    position: absolute;
    top: 0;
    height: 294px;
  }
  .swatch--navy { left: 0; width: 602px; background: var(--navy); }
  .swatch--red { left: 602px; width: 598px; background: var(--red); }

  .card {
    position: absolute;
    top: 558px;
    width: 518px;
    height: 310px;
    background: var(--card);
    box-shadow: 8px 8px 8px var(--shadow);
  }
  .card--front { left: 58px; }
  .card--back { left: 625px; }

  .brand-name {
    position: absolute;
    left: 46px;
    top: 50px;
    font-size: 44px;
    line-height: 0.98;
    letter-spacing: 1.5px;
    text-transform: uppercase;
    color: var(--navy);
  }
  .company-line {
    position: absolute;
    right: 35px;
    top: 256px;
    font-size: 16.5px;
    letter-spacing: 1.6px;
  }

  .person-name {
    position: absolute;
    left: 37px;
    top: 24px;
    font-size: 25px;
    letter-spacing: 1.6px;
  }
  .person-title {
    position: absolute;
    left: 37px;
    top: 58px;
    font-size: 16px;
    letter-spacing: 2.2px;
  }
  .contact {
    position: absolute;
    left: 37px;
    font-size: 16px;
    letter-spacing: 1.9px;
    line-height: 19px;
  }
  .contact--phone { top: 161px; }
  .contact--online { top: 200px; }
  .contact--services { top: 259px; }
</style>
</head>
<body>
  <div class="swatch swatch--navy"></div>
  <div class="swatch swatch--red"></div>

  <section class="card card--front">
    <div class="brand-name">Harbourline<br>Strategy Group</div>
    <p class="company-line">Harbourline Strategy Group Pty Ltd</p>
  </section>

  <section class="card card--back">
    <h1 class="person-name">Daniel Ferreira</h1>
    <p class="person-title">Principal Consultant</p>
    <p class="contact contact--phone">+61 417 260 315</p>
    <p class="contact contact--online">daniel@harbourlinestrategygroup.com.au<br>www.harbourlinestrategygroup.com</p>
    <p class="contact contact--services">Professional services: Business Analysis, Strategic Advisory</p>
  </section>
</body>
</html>
```